The Bright Meadow Foundation

This is a non profit . We are a 501(c)(3) charitable organization in the United States. The organization is a volunteer based group providing basic healthcare to those living in underserved rural areas around the world. I have attached a brochure that provides some information about the organization. We are looking for a basic 5 page web page Page 1 Photos that fade into the next x 3 with mission statementPage 2 About us - details about bright meadow foundation. also introducing our Founders of the organization. Marina Kellet, M.D. Dorla Penn , FNP, Rosa Tembley, FNP, Wade Marlow. ( will provide you info on each.Page 3 Projects coming up and futurePage 4 Get involved - Give a donation, Volunteer, Corporate supportPage 5 Support us and contact us with a message box.We mainly work in South America but anticipate trave to South Africa in the near future. Colors bright with emphasis on Reds and Purples. I have attached some photos and ideas. You can use or not use ok to use something similar if you so like

Target Market(s)

People interested in volunteering time or money to overseas medical work. NOT a religious base

Coding

Coded - Design and coding required

Number of Pages Required

1 page

Colors
876aae
ec1f27
f37022
9bcb3c

Requirements
Must have
• Colorful pictures nature, brings out emotion, colorful, children from various parts of the world, animals.
• Tried to down load some pictures but would not go thru.

```html
<!DOCTYPE html>
<html lang="en">
<head>
<meta charset="utf-8">
<title>The Bright Meadow Foundation</title>
<link href="https://fonts.googleapis.com/css2?family=Poppins:wght@300;400;500;600;700;800&family=Montserrat:wght@800;900&display=swap" rel="stylesheet">
<style>
:root{
  --purple:#876aae;
  --orange:#f37022;
  --red:#ec1f27;
  --green:#9bcb3c;
  --ink:#222;
  --muted:#777;
  --dark:#2a2a2a;
  --darker:#1c1c1c;
}
*{box-sizing:border-box;margin:0;padding:0}
html,body{width:1200px;height:5372px;overflow:hidden}
body{font-family:'Poppins',sans-serif;color:var(--ink);background:#fff;position:relative}
.abs{position:absolute}
.btn{display:inline-flex;align-items:center;justify-content:center;background:var(--orange);color:#fff;font-weight:600;border-radius:24px;font-size:15px}
.ph{position:absolute}

/* top bar */
.topbar{position:absolute;top:0;left:0;width:1200px;height:50px;background:var(--purple);color:#fff;font-size:12px}
.topbar .contact{position:absolute;left:95px;top:16px;display:flex;gap:30px;align-items:center}
.topbar .contact span{display:flex;gap:8px;align-items:center}
.topbar .social{position:absolute;right:92px;top:13px;display:flex;gap:10px}
.topbar .social i{width:24px;height:24px;border-radius:50%;background:#fff;display:block}

/* nav */
.nav{position:absolute;top:50px;left:0;width:1200px;height:80px;background:#fff}
.brand{position:absolute;left:92px;top:20px;display:flex;align-items:center;gap:10px;color:var(--purple);font-weight:600;font-size:15px;line-height:1.1}
.brand i{width:30px;height:30px;border-radius:50%;background:var(--purple);display:block}
.menu{position:absolute;left:305px;top:30px;display:flex;gap:40px;font-size:12px;font-weight:500;align-items:center}
.menu .on{background:var(--orange);color:#fff;padding:2px 10px;border-radius:10px}
.nav .donate{position:absolute;left:950px;top:18px;width:157px;height:46px;font-size:17px}

/* hero */
.hero{position:absolute;top:130px;left:0;width:1200px;height:470px;background:linear-gradient(90deg,#8f8f8f 0%,#5a5a5a 40%,#3a3a3a 100%)}
.hero h1{position:absolute;left:510px;top:100px;font-family:'Montserrat',sans-serif;font-weight:900;color:#fff;font-size:92px;letter-spacing:3px;line-height:1}
.hero h2{position:absolute;left:512px;top:200px;font-family:'Montserrat',sans-serif;font-weight:900;color:#fff;font-size:62px;letter-spacing:3px;line-height:1}
.hero p{position:absolute;left:512px;top:272px;color:#fff;font-size:23px;font-weight:300}
.dots{position:absolute;left:568px;top:432px;display:flex;gap:8px}
.dots i{width:13px;height:13px;border-radius:50%;background:#fff;display:block}
.dots i:first-child{background:var(--green)}

/* feature cards */
.feature{position:absolute;top:680px;width:310px;height:220px;background:#fff;box-shadow:0 6px 16px rgba(0,0,0,.12);border-bottom:3px solid var(--purple);text-align:center}
.feature svg{margin-top:30px}
.feature h3{font-size:11px;font-weight:600;margin-top:8px}
.feature p{font-size:11px;color:var(--muted);padding:0 38px;margin-top:18px;line-height:1.65}
.feature .go{position:absolute;left:143px;bottom:-10px;width:24px;height:24px;border-radius:50%;background:#fff;border:1px solid #ccc;display:flex;align-items:center;justify-content:center;color:var(--green);font-size:13px}

/* section headings */
.eyebrow{display:flex;align-items:center;gap:14px;font-size:17px;font-weight:600}
.eyebrow::after{content:"";width:58px;height:5px;border-top:2px solid var(--green);border-bottom:2px solid var(--green)}
.title{font-size:40px;font-weight:600}
.body{font-size:11.5px;color:#555;line-height:22px}
.center-head{position:absolute;left:0;width:1200px;text-align:center}
.center-head .mark{display:flex;justify-content:center;align-items:center;gap:22px}
.center-head .mark .ln{width:58px;height:7px;border-top:2px solid #333;border-bottom:2px solid #333}

/* projects */
.proj{position:absolute;top:1660px;width:240px;text-align:center}
.proj .img{height:212px}
.proj h4{font-size:17px;font-weight:600;margin-top:22px}
.proj .date{font-size:16px;color:#555;margin-top:6px}
.proj p{font-size:10.5px;color:#666;line-height:17px;margin-top:22px;padding:0 4px}
.proj .btn{width:156px;height:44px;margin-top:22px;font-size:16px}

/* stats */
.stats{position:absolute;top:2198px;left:0;width:1200px;height:348px;background:linear-gradient(90deg,#3d3d3d,#555 50%,#3a3a3a)}
.stat{position:absolute;top:138px;display:flex;gap:14px;align-items:center;color:#fff}
.stat b{display:block;font-size:29px;font-weight:400;line-height:1.15}

/* founders */
.founder{position:absolute;top:2762px;width:497px;height:610px;background:#fff;box-shadow:0 8px 18px rgba(0,0,0,.1);text-align:center}
.founder .img{height:328px}
.founder h4{font-size:25px;font-weight:500;margin-top:34px}
.founder p{font-size:11px;color:#666;line-height:19px;padding:0 28px;margin-top:18px}
.founder .btn{width:132px;height:38px;margin-top:26px;font-size:14px}
.arrows{position:absolute;display:flex;gap:10px}
.arrows i{width:48px;height:36px;display:flex;align-items:center;justify-content:center;font-style:normal;color:#fff;font-size:18px}
.arrows .prev{background:#e6e6e6}
.arrows .next{background:var(--green)}

/* get involved */
.gi-card{position:absolute;top:3700px;width:255px;height:190px;background:#fff;box-shadow:0 6px 16px rgba(0,0,0,.1);padding:14px 12px}
.gi-card h5{font-size:20px;font-weight:500}
.gi-card .by{font-size:14px;font-weight:600;color:#444;margin-top:4px}
.gi-card .by em{color:var(--purple);font-style:normal}
.gi-card p{font-size:11px;color:#666;line-height:19px;margin-top:12px}
.gi-card .btn{width:130px;height:38px;margin-top:10px;font-size:13px}

/* contact */
.contact-box{position:absolute;top:4038px;left:93px;width:1014px;height:554px;background:#f7f7f7}
.contact-info{position:absolute;left:35px;top:150px;width:420px}
.contact-info h3{font-size:22px;font-weight:500}
.contact-info p{font-size:11px;color:#666;line-height:19px;margin-top:16px}
.ci-row{display:flex;gap:16px;align-items:flex-start;font-size:11px;color:#333;margin-top:40px;line-height:17px}
.form{position:absolute;left:509px;top:0;width:505px;height:554px;background:var(--red);color:#fff;padding:40px 45px}
.form .field{border-bottom:1px solid rgba(255,255,255,.8);height:58px;padding-top:26px;font-size:15px}
.form .field:first-child{padding-top:0;height:32px}
.form .msg{border:1px solid rgba(255,255,255,.8);height:142px;margin-top:38px;padding:14px 18px;font-size:15px}
.form .send{display:flex;align-items:center;justify-content:center;width:130px;height:40px;background:#fff;color:var(--red);border-radius:22px;font-weight:600;font-size:15px;margin:30px 0 0 10px}

/* newsletter */
.news{position:absolute;top:4685px;left:0;width:1200px;height:220px;background:linear-gradient(90deg,#333,#444 60%,#333);color:#fff}
.news h3{position:absolute;left:93px;top:80px;font-size:34px;font-weight:600}
.news p{position:absolute;left:93px;top:128px;font-size:11px;line-height:17px}
.news .email{position:absolute;left:740px;top:77px;width:367px;height:60px;border:1px solid #fff;border-radius:30px;font-size:11px;padding:20px 30px}

/* footer */
.footer{position:absolute;top:4905px;left:0;width:1200px;height:438px;background:var(--dark);color:#fff}
.footer h5{font-size:17px;font-weight:600}
.footer .col{position:absolute;top:118px}
.footer .about{position:absolute;left:93px;top:100px;width:250px}
.footer .about .fbrand{font-size:22px;font-weight:600}
.footer .about p{font-size:11px;line-height:24px;margin-top:36px;color:#ddd}
.footer .circles{display:flex;gap:14px;margin-top:22px}
.footer .circles i{width:38px;height:38px;border-radius:50%;background:#fff;display:block}
.footer ul{list-style:none;margin-top:28px}
.footer li{font-size:11px;display:flex;align-items:center;gap:12px;height:47px;color:#ddd}
.post{display:flex;gap:12px;margin-top:26px}
.post .thumb{width:78px;height:78px;flex:none}
.post span{font-size:11px;line-height:16px;color:#ddd}
.post b{display:block;font-size:14px;font-weight:600;margin-top:6px;color:#fff}
.founders-list li{height:50px}
.bottom{position:absolute;top:5343px;left:0;width:1200px;height:29px;background:var(--darker);color:#fff;font-size:10px;text-align:center;line-height:29px}
</style>
</head>
<body>

<div class="topbar">
  <div class="contact">
    <span><svg width="10" height="14" viewBox="0 0 10 14"><path d="M3 1 L1 3 C1 8 4 12 8 13 L10 11 L7 9 L6 10 C4 9 3 7 3 5 L4 4 Z" fill="#fff"/></svg>1-555-014-2290</span>
    <span><svg width="16" height="11" viewBox="0 0 16 11"><rect x=".5" y=".5" width="15" height="10" fill="none" stroke="#fff"/><path d="M1 1 L8 6 L15 1" fill="none" stroke="#fff"/></svg>info@brightmeadowfoundation.org</span>
  </div>
  <div class="social"><i></i><i></i></div>
</div>

<div class="nav">
  <div class="brand"><i></i><span>Bright Meadow<br>Foundation</span></div>
  <div class="menu"><span class="on">Home</span><span>About Us</span><span>Projects</span><span>Get involved</span><span>Support us and contact us</span></div>
  <span class="btn donate">Donation</span>
</div>

<section class="hero" role="img" aria-label="Black and white photo of a smiling young child in a knit hat waving">
  <h1>HEALTHCARE</h1>
  <h2>TO THOSE</h2>
  <p>Living in underserved Rural areas around the world.</p>
  <div class="dots"><i></i><i></i><i></i></div>
</section>

<div class="feature" style="left:95px">
  <svg width="40" height="44" viewBox="0 0 40 44" fill="none" stroke="#876aae" stroke-width="2"><path d="M20 22 C10 14 12 6 20 11 C28 6 30 14 20 22Z"/><path d="M2 30 H12 L22 34 H32 L38 30 M12 30 V42 H2"/></svg>
  <h3>Donation</h3>
  <p>Lorem ipsum is simply dummy text of the printing and typesetting industry. Lorem ipsum has been the</p>
  <span class="go">→</span>
</div>
<div class="feature" style="left:445px">
  <svg width="44" height="44" viewBox="0 0 44 44" fill="none" stroke="#876aae" stroke-width="2"><path d="M22 20 C12 12 14 4 22 9 C30 4 32 12 22 20Z"/><path d="M4 22 V36 L12 42 M40 22 V36 L32 42 M10 26 L16 34 M34 26 L28 34"/></svg>
  <h3>Volunteer</h3>
  <p>Lorem ipsum is simply dummy text of the printing and typesetting industry. Lorem ipsum has been the</p>
  <span class="go">→</span>
</div>
<div class="feature" style="left:795px">
  <svg width="44" height="44" viewBox="0 0 44 44" fill="none" stroke="#876aae" stroke-width="2"><path d="M22 24 C12 16 14 8 22 13 C30 8 32 16 22 24Z"/><path d="M4 14 V30 L14 40 M40 14 V30 L30 40 M8 8 L14 20 M36 8 L30 20"/></svg>
  <h3>Corporate</h3>
  <p>Lorem ipsum is simply dummy text of the printing and typesetting industry.</p>
  <span class="go">→</span>
</div>

<!-- about -->
<div class="ph" style="left:0;top:980px;width:433px;height:315px;background:linear-gradient(135deg,#6b8a5a,#c9584a 50%,#4a5c7a)" role="img" aria-label="Group photo of volunteers standing outdoors"></div>
<div class="ph" style="left:276px;top:1166px;width:232px;height:224px;background:#fff;box-shadow:0 4px 12px rgba(0,0,0,.15)"></div>
<div class="ph" style="left:282px;top:1172px;width:220px;height:212px;background:linear-gradient(135deg,#8a7060,#4c3f3a 60%,#b79a80)" role="img" aria-label="Volunteer with local women and children indoors"></div>
<div class="abs" style="left:590px;top:1000px">
  <div class="eyebrow">Charity with Mission</div>
  <div class="title" style="margin-top:20px">About Us</div>
  <p class="body" style="width:520px;margin-top:14px">The Bright Meadow Foundation was founded with the aim of helping rural and indigenous individuals in various parts of the world. The Foundation's vision is to see that every woman, man and child have access to basic medical care and treatment as well as fundamental knowledge in preventative care. There are many people living in regions of the world today who have limited or no access to health centers. Often, these individuals travel hours and in many instances days for basic care that often times can be averted with preventative care measures.</p>
  <span class="btn" style="width:157px;height:44px;margin-top:24px">Read More</span>
</div>

<!-- projects -->
<div class="center-head" style="top:1472px">
  <div class="mark"><span class="ln"></span><svg width="40" height="36" viewBox="0 0 40 36"><path d="M20 35 C4 22 0 14 4 7 C8 0 17 1 20 8 C23 1 32 0 36 7 C40 14 36 22 20 35Z" fill="#876aae"/></svg><span class="ln"></span></div>
  <div class="title" style="margin-top:12px">Project</div>
  <p style="font-size:11px;color:#555;margin-top:10px;line-height:18px">Lorem Ipsum is simply dummy text of the printing and typesetting industry<br>Lorem Ipsum is simply dummy text of the printing and typesetting industry. Lorem Ipsum</p>
</div>
<div class="proj" style="left:93px"><div class="img" style="background:linear-gradient(135deg,#8aa0b8,#3c4452)" role="img" aria-label="Volunteers with luggage on a street"></div><h4>Lorem Ipsum</h4><div class="date">02.08.2019</div><p>"Lorem ipsum dolor sit amet, consectetur adipiscing elit, sed do eiusmod tempor incididunt ut labore et dolore magna aliqua. Ut enim ad minim veniam,</p><span class="btn">Donation</span></div>
<div class="proj" style="left:351px"><div class="img" style="background:linear-gradient(135deg,#9db3c9,#b8b2a8)" role="img" aria-label="Supplies loaded on top of a van"></div><h4>Lorem Ipsum</h4><div class="date">02.08.2019</div><p>"Lorem ipsum dolor sit amet, consectetur adipiscing elit, sed do eiusmod tempor incididunt ut labore et dolore magna aliqua. Ut enim ad minim veniam,</p><span class="btn">Donation</span></div>
<div class="proj" style="left:610px"><div class="img" style="background:linear-gradient(135deg,#a04048,#5c3a38)" role="img" aria-label="Nurse treating a patient in a clinic"></div><h4>Lorem Ipsum</h4><div class="date">02.08.2019</div><p>"Lorem ipsum dolor sit amet, consectetur adipiscing elit, sed do eiusmod tempor incididunt ut labore et dolore magna aliqua. Ut enim ad minim veniam,</p><span class="btn">Donation</span></div>
<div class="proj" style="left:868px"><div class="img" style="background:linear-gradient(135deg,#d8a23a,#b03a6a 60%,#5a7aa0)" role="img" aria-label="Woman in colorful traditional dress with a child"></div><h4>Lorem Ipsum</h4><div class="date">02.08.2019</div><p>"Lorem ipsum dolor sit amet, consectetur adipiscing elit, sed do eiusmod tempor incididunt ut labore et dolore magna aliqua. Ut enim ad minim veniam,</p><span class="btn">Donation</span></div>

<!-- stats -->
<section class="stats" role="img" aria-label="Dark photo of volunteers raising hands">
  <div class="stat" style="left:93px"><svg width="66" height="66" viewBox="0 0 66 66" fill="none" stroke="#fff" stroke-width="3"><circle cx="20" cy="16" r="8"/><circle cx="44" cy="16" r="8"/><path d="M6 44 C6 30 34 30 34 44 M30 34 C34 28 58 28 58 40"/><circle cx="44" cy="50" r="12"/><circle cx="44" cy="50" r="4"/></svg><div><b>Ngo</b><b>254565</b></div></div>
  <div class="stat" style="left:362px"><svg width="56" height="66" viewBox="0 0 56 66" fill="none" stroke="#fff" stroke-width="3"><rect x="4" y="28" width="48" height="34"/><path d="M16 28 V6 H40 V28"/><circle cx="28" cy="17" r="6"/></svg><div><b>Donation</b><b>254565</b></div></div>
  <div class="stat" style="left:618px"><svg width="66" height="66" viewBox="0 0 66 66" fill="#fff"><circle cx="14" cy="10" r="6"/><circle cx="33" cy="8" r="6"/><circle cx="52" cy="10" r="6"/><rect x="8" y="18" width="12" height="26"/><rect x="27" y="16" width="12" height="28"/><rect x="46" y="18" width="12" height="26"/><rect x="9" y="44" width="4" height="20"/><rect x="15" y="44" width="4" height="20"/><rect x="28" y="44" width="4" height="20"/><rect x="34" y="44" width="4" height="20"/><rect x="47" y="44" width="4" height="20"/><rect x="53" y="44" width="4" height="20"/></svg><div><b>Volunteer</b><b>254565</b></div></div>
  <div class="stat" style="left:902px"><svg width="66" height="66" viewBox="0 0 66 66" fill="#fff"><circle cx="20" cy="10" r="7"/><path d="M14 20 H26 L34 34 L44 40 L40 44 L28 38 L26 62 H20 L18 44 L10 62 H4 Z"/><circle cx="50" cy="42" r="6"/><path d="M42 52 H60 L62 62 H40 Z"/></svg><div><b>Help</b><b>254565</b></div></div>
</section>

<!-- founders -->
<div class="center-head" style="top:2652px">
  <div class="mark"><span class="ln"></span><svg width="40" height="36" viewBox="0 0 40 36"><path d="M20 35 C4 22 0 14 4 7 C8 0 17 1 20 8 C23 1 32 0 36 7 C40 14 36 22 20 35Z" fill="#876aae"/></svg><span class="ln"></span></div>
  <div class="title" style="margin-top:8px">Founder</div>
</div>
<div class="arrows" style="left:1000px;top:2710px"><i class="prev">‹</i><i class="next">›</i></div>
<div class="founder" style="left:93px">
  <div class="img" style="background:linear-gradient(135deg,#c85a2a,#e08a3a 50%,#6a3a2a)" role="img" aria-label="Portrait of co-founder Dorla Penn"></div>
  <h4>DORLA PENN , FNP ( CO - FOUNDER )</h4>
  <p>Dorla Penn is a Nurse Practitioner who is currently practicing in her home state of Colorado. Dorla has spent many years working with underserved populations and has a passion for serving in her global community. Dorla graduated from Front Range State University with a Bachelor's in Nursing. Dorla initially worked in the oncology field but soon determined that she desired a more on-going relationship with the people that she cared for.</p>
  <span class="btn">Read More</span>
</div>
<div class="founder" style="left:610px">
  <div class="img" style="background:linear-gradient(135deg,#e040a0,#5a3ac8 50%,#2a9ad8)" role="img" aria-label="Portrait of co-founder Wade Marlow"></div>
  <h4>WADE MARLOW ( CO - FOUNDER )</h4>
  <p>Wade Marlow is a stylist and make-up artist in Boulder ,Colorado. He has always had a passion for helping others. Upon finishing high school, he obtained his Certified Nursing Assistant through Valley Technical College. He worked in a private nursing home for 3 years where his Wade Marlow is a stylist and make-up artist in Boulder ,Colorado. He has always had a passion for helping others. Upon finishing high school, he obtained his Certified Nursing Assistant</p>
  <span class="btn">Read More</span>
</div>

<!-- get involved -->
<div class="ph" style="left:0;top:3460px;width:548px;height:492px;background:linear-gradient(135deg,#7a5a48,#c0a07a 45%,#6a4a8a)" role="img" aria-label="Volunteer kneeling with young girls in traditional dress"></div>
<div class="abs" style="left:588px;top:3470px">
  <div style="display:flex;gap:22px;align-items:center"><svg width="40" height="36" viewBox="0 0 40 36"><path d="M20 35 C4 22 0 14 4 7 C8 0 17 1 20 8 C23 1 32 0 36 7 C40 14 36 22 20 35Z" fill="#876aae"/></svg><span style="width:58px;height:7px;border-top:2px solid #333;border-bottom:2px solid #333"></span></div>
  <div class="eyebrow" style="margin-top:18px">Charity with Mission</div>
  <div class="title" style="margin-top:12px">Get Involved</div>
  <p class="body" style="width:520px;font-size:10.5px;line-height:17px;margin-top:6px">It is a long established fact that a reader will be distracted by the readable content of a page when looking at its layout. The point of using Lorem Ipsum is that it has a more-or-less normal distribution of letters</p>
</div>
<div class="gi-card" style="left:588px"><h5>Give a Donation</h5><div class="by"><em>Organized By</em> ; Bright Meadow</div><p>Lorem Ipsum is simply dummy text of the printing and typesetting industry. Lorem Ipsum has bee</p><span class="btn">Join Us</span></div>
<div class="gi-card" style="left:852px"><h5>Volunteer</h5><div class="by"><em>Organized By</em> ; Bright Meadow</div><p>Lorem Ipsum is simply dummy text of the printing and typesetting industry. Lorem Ipsum has bee</p><span class="btn">Join Us</span></div>
<div class="arrows" style="left:588px;top:3916px"><i class="prev">‹</i><i class="next">›</i></div>

<!-- contact -->
<div class="contact-box">
  <div class="contact-info">
    <h3>Lets Get In Touch</h3>
    <p>There are many variations of passages of Lorem Ipsum available, but the majority have suffered alteration in some form, by injected humour,</p>
    <div class="ci-row" style="margin-top:88px"><svg width="14" height="18" viewBox="0 0 14 18"><path d="M7 17 C2 10 1 8 1 6 A6 6 0 0 1 13 6 C13 8 12 10 7 17Z" fill="#222"/><circle cx="7" cy="6" r="2" fill="#fff"/></svg><span>4820 Meadow Ridge Rd, Alder Creek, CO,<br>80412</span></div>
    <div class="ci-row"><svg width="10" height="16" viewBox="0 0 10 14"><path d="M3 1 L1 3 C1 8 4 12 8 13 L10 11 L7 9 L6 10 C4 9 3 7 3 5 L4 4 Z" fill="#222"/></svg><span>1-555-014-2290</span></div>
    <div class="ci-row"><svg width="16" height="11" viewBox="0 0 16 11"><rect x=".5" y=".5" width="15" height="10" fill="none" stroke="#222"/><path d="M1 1 L8 6 L15 1" fill="none" stroke="#222"/></svg><span>info@brightmeadowfoundation.org</span></div>
  </div>
  <div class="form">
    <div class="field">Name</div>
    <div class="field">Last Name</div>
    <div class="field">Phone</div>
    <div class="field">Email</div>
    <div class="msg">Massege</div>
    <span class="send">Send</span>
  </div>
  <svg class="abs" style="left:485px;top:70px" width="26" height="40" viewBox="0 0 26 40"><path d="M26 0 V40 L0 20 Z" fill="#ec1f27"/></svg>
</div>

<!-- newsletter -->
<section class="news">
  <h3>Subscribe to Newsletter</h3>
  <p>It is a long established fact that a reader will be distracted<br>by the readable content of a page when looking at its layout. The point of using</p>
  <div class="email">Enter Your Email
    <span class="abs" style="left:285px;top:12px;width:1px;height:34px;background:#fff"></span>
    <svg class="abs" style="left:305px;top:16px" width="30" height="28" viewBox="0 0 30 28"><path d="M1 14 L29 1 L20 27 L14 17 Z" fill="#f37022"/></svg>
  </div>
</section>

<!-- footer -->
<footer class="footer">
  <div class="about">
    <div style="display:flex;gap:10px;align-items:center"><i style="width:34px;height:34px;border-radius:50%;background:#fff;display:block"></i><span class="fbrand">Bright Meadow</span></div>
    <p>Your donations allow us to provide medical care, health resources and supplies, and wellness education to the communities we serve. The links below are some of the ways you can donate to our organization.</p>
    <div class="circles"><i></i><i></i></div>
  </div>
  <div class="col" style="left:430px"><h5>Site Map</h5>
    <ul><li>➜ Home</li><li>➜ About Us</li><li>➜ Project</li><li>➜ Get Involved</li><li>➜ Support us and Contact us</li></ul></div>
  <div class="col" style="left:642px"><h5>Recent Post</h5>
    <div class="post"><div class="thumb" style="background:linear-gradient(135deg,#8a6a5a,#4a4a6a)" role="img" aria-label="Clinic visit photo"></div><span>Lorem Ipsum is simply dummy text of the printing and typesetting<b>10.07.2019</b></span></div>
    <div class="post"><div class="thumb" style="background:linear-gradient(135deg,#6a8aa8,#8a5a4a)" role="img" aria-label="Volunteers working photo"></div><span>Lorem Ipsum is simply dummy text of the printing and typesetting<b>10.07.2019</b></span></div>
  </div>
  <div class="col" style="left:940px"><h5>Founders</h5>
    <ul class="founders-list"><li>Marina Kellet</li><li>M.D. Dorla Penn FNP</li><li>Rosa Tembley FNP</li><li>Wade Marlow</li></ul></div>
</footer>
<div class="bottom">© CopyRight 2019 Bright Meadow , Allright Reserved</div>

</body>
</html>
```